Business Card Design - R.T. Custom Cabinets Ltd.

Design a business card, including a new logo for a new company in Vancouver, British Columbia, Canada.

The logo must be available as a separate file.

The card should include all company information including:
R.T. Custom Cabinets Ltd.
2786 Larchmoor Crescent
Burnaby, B.C. V7K 2P9
Telehone: 604-XXX-XXXX
Fax: 604-XXX-XXXX
www.rtcustomcabinets.example

As well as individual contact information for employees:
Name
Position
Telephone
Email

The card must include a thoughtful message as well

Target Market(s)

Custom Cabinets

Industry/Entity Type

Business

Contact Information for Business Card

Important information on the front, thoughtful message on the back

Colors
fbed22
9bcb3c
0355a3
ec1f27

Requirements
Must have
• See project description
Nice to have
• images that showcase custom cabinets (european, modern and traditional) styles

```html
<!DOCTYPE html>
<html lang="en">
<head>
<meta charset="utf-8">
<title>R.T. Custom Cabinets Ltd. – Business Card</title>
<link rel="stylesheet" href="https://fonts.googleapis.com/css2?family=Open+Sans:wght@400;600;700;800&display=swap">
<style>
  :root {
    --backdrop: #cdcdcd;
    --brand-blue: #0355a3;
    --brand-red: #ec1f27;
    --ink: #3a3a3a;
    --card-white: #f4f4f4;
    --back-start: #d4303a;
    --back-end: #5e4670;
  }
  * { box-sizing: border-box; margin: 0; padding: 0; }
  html, body { width: 1200px; height: 1200px; overflow: hidden; }
  body {
    background: var(--backdrop);
    font-family: "Open Sans", Arial, sans-serif;
    position: relative;
  }
  .card {
    position: absolute;
    border-radius: 3px;
    box-shadow: 0 14px 30px rgba(0,0,0,0.18);
  }
  /* Back of card */
  .card-back {
    left: 60px; top: 80px; width: 560px; height: 320px;
    background: linear-gradient(100deg, var(--back-start) 0%, #9a3f5a 55%, var(--back-end) 100%);
    display: flex; flex-direction: column; align-items: center; justify-content: center; gap: 14px;
    color: #ffffff; text-align: center;
  }
  .card-back .wordmark { font-size: 34px; font-weight: 800; }
  .card-back .message { font-size: 17px; font-weight: 400; opacity: 0.92; }
  /* Front of card */
  .card-front {
    left: 380px; top: 440px; width: 760px; height: 434px;
    background: linear-gradient(160deg, #ffffff 0%, var(--card-white) 45%, #e9e9e9 100%);
    overflow: hidden;
  }
  .edge-band {
    position: absolute; left: 0; top: 0; bottom: 0; width: 16px;
    background: var(--brand-red);
    border-right: 4px solid #ffffff;
    box-shadow: 2px 0 0 var(--brand-blue);
  }
  .front-wordmark {
    position: absolute; left: 50px; top: 60px;
    color: var(--brand-blue); font-size: 44px; font-weight: 800; line-height: 1;
  }
  .rule {
    position: absolute; left: 44px; right: 0; height: 1px; background: var(--brand-red); opacity: 0.7;
  }
  .rule-top { top: 250px; }
  .rule-bottom { top: 340px; }
  .person {
    position: absolute; left: 50px; top: 282px;
    display: flex; align-items: baseline; gap: 14px;
  }
  .person-name { font-size: 34px; font-weight: 700; color: var(--brand-blue); }
  .person-name .surname { color: var(--brand-red); }
  .person-sep { width: 3px; height: 30px; background: var(--brand-red); align-self: center; }
  .person-role { font-size: 20px; color: #555; }
  .contact-col {
    position: absolute; top: 358px;
    display: flex; flex-direction: column; gap: 10px;
    font-size: 16px; color: var(--ink);
  }
  .contact-col.phones { left: 50px; }
  .contact-col.web { left: 230px; border-left: 1px solid #e3a0a3; padding-left: 14px; }
  .contact-col.address {
    left: 500px; top: 266px; gap: 4px;
    border-left: 1px solid #e3a0a3; padding-left: 14px; line-height: 1.45;
  }
  .contact-row { display: flex; align-items: center; gap: 8px; white-space: nowrap; }
  .address-line { padding-left: 24px; white-space: nowrap; }
  .contact-row svg { width: 16px; height: 16px; flex: none; fill: var(--brand-red); }
  /* Standalone logo lockup */
  .logo-lockup {
    position: absolute; right: 40px; top: 1060px;
    display: flex; align-items: center; gap: 14px;
  }
  .logo-lockup .mark-dot { width: 22px; height: 22px; background: var(--brand-blue); }
  .logo-lockup .wordmark { color: var(--brand-blue); font-size: 34px; font-weight: 800; }
</style>
</head>
<body>

<section class="card card-back" aria-label="Card back">
  <span class="wordmark">R.T. Custom Cabinets Ltd.</span>
  <span class="message">Crafted with care, built to last a lifetime.</span>
</section>

<section class="card card-front" aria-label="Card front">
  <div class="edge-band"></div>
  <div class="front-wordmark">R.T. Custom<br>Cabinets Ltd.</div>

  <div class="person">
    <span class="person-name">ALEX <span class="surname">MORROW</span></span>
    <span class="person-sep"></span>
    <span class="person-role">Director</span>
  </div>

  <div class="contact-col address">
    <div class="contact-row">
      <svg viewBox="0 0 16 16"><path d="M8 1 1 7.5h2V15h4v-4h2v4h4V7.5h2z"/></svg>
      2786 Larchmoor Crescent
    </div>
    <div class="address-line">Burnaby, B.C. V7K 2P9</div>
  </div>

  <div class="rule rule-top"></div>
  <div class="rule rule-bottom"></div>

  <div class="contact-col phones">
    <div class="contact-row">
      <svg viewBox="0 0 16 16"><path d="M3.6 1.5 6 4 4.8 5.8c.8 1.9 2.4 3.5 4.4 4.4L11 9l2.5 2.4-1.6 2.6C6.4 13.6 2.4 9.6 1.9 3.1z"/></svg>
      604-XXX-XXXX
    </div>
    <div class="contact-row">
      <svg viewBox="0 0 16 16"><path d="M4 1h8v4H4zM1 6h14v6h-3v3H4v-3H1zm4 4v4h6v-4z"/></svg>
      604-XXX-XXXX
    </div>
  </div>

  <div class="contact-col web">
    <div class="contact-row">
      <svg viewBox="0 0 16 16"><path d="M1 3h14v10H1zm1.5 1.2V5L8 9l5.5-4v-.8L8 8z"/></svg>
      alex@rtcustomcabinets.example
    </div>
    <div class="contact-row">
      <svg viewBox="0 0 16 16"><path d="M8 1a7 7 0 1 0 0 14A7 7 0 0 0 8 1zm0 1.3c.8 0 1.7 1.6 2 4.2H6c.3-2.6 1.2-4.2 2-4.2zM6 8.5h4c-.1 2.8-1.1 5.2-2 5.2S6.1 11.3 6 8.5zM2.5 6.5A5.7 5.7 0 0 1 5.8 2.8c-.5 1-.9 2.3-1 3.7zm8.7 0c-.1-1.4-.5-2.7-1-3.7a5.7 5.7 0 0 1 3.3 3.7zM2.5 9.5h2.3c.1 1.4.5 2.7 1 3.7a5.7 5.7 0 0 1-3.3-3.7zm8.7 0h2.3a5.7 5.7 0 0 1-3.3 3.7c.5-1 .9-2.3 1-3.7z"/></svg>
      www.rtcustomcabinets.example
    </div>
  </div>
</section>

<div class="logo-lockup" aria-label="Company logo">
  <span class="mark-dot"></span>
  <span class="wordmark">R.T. Custom Cabinets Ltd.</span>
</div>

</body>
</html>
```